Business card design for global fintech startup

Veltrix is a modern payments platform for the global insurance industry, serving international health, life, and travel insurers, MGAs, brokers, and partners.

We need a professional, premium business card for use at insurance conferences and executive meetings. The goal is to create a card that feels trustworthy, modern, and high-quality, while still being distinctive and memorable in a stack of business cards.

Target audience:
Senior insurance executives (VP, C-suite).

Design goals:
Clear, professional, and credible
Modern but not trendy
Premium and well-structured
Easy to read and practical for networking

Brand direction:
Brand-first (company over individual)
Follow existing brand guidelines where possible
Clean layout, strong hierarchy, excellent readability

Must include:
Name
Title
Company name (Veltrix)
Logo
Email
Phone/Whatsapp
Website (www.withveltrix.example)
Tagline - Confidence in motion

Materials & finish:
Open to designer recommendations for premium look and feel.

Please avoid:
Flashy or trendy startup styles
Generic insurance icons or clichés
Cluttered layouts or hard-to-read text

Deliverables:
Front and back business card, print-ready files.

Target Market(s)

Global Insurance executives

Industry/Entity Type

Fintech, Insurtech, Insurance, Financial Services

Contact Information for Business Card

Name Title Company name (Veltrix) Logo Email Phone/Whatsapp Website (www.withveltrix.example) Tagline - Confidence in motion

Font styles to use
Other font styles liked:
• See brand guidelines

Requirements
Nice to have
• something that stands out/makes us more memorable while still remaining professional
Should not have
• Please avoid: Flashy or trendy startup styles Generic insurance icons or clichés Cluttered layouts or hard-to-read text

```html
<!DOCTYPE html>
<html lang="en">
<head>
<meta charset="UTF-8">
<title>Veltrix Business Card</title>
<link href="https://fonts.googleapis.com/css2?family=Montserrat:wght@400;500;600;800&display=swap" rel="stylesheet">
<style>
  :root {
    --bg: #e4e4e4;
    --card-white: #ffffff;
    --card-black: #141414;
    --brand-blue: #1e7fd0;
    --text-dark: #1c1c1c;
    --text-grey: #8a8a8a;
    --text-light: #ffffff;
    --accent-cyan: #14c8f0;
  }
  * { box-sizing: border-box; margin: 0; padding: 0; }
  html, body { width: 1200px; height: 800px; overflow: hidden; }
  body {
    background: var(--bg);
    font-family: "Montserrat", Arial, sans-serif;
    display: flex;
    align-items: center;
    justify-content: center;
    gap: 60px;
  }
  .card {
    width: 500px;
    height: 286px;
    border-radius: 14px;
    position: relative;
    overflow: hidden;
    box-shadow: 0 4px 14px rgba(0,0,0,0.12);
  }
  /* Front */
  .card--front { background: var(--card-white); }
  .card__tab {
    position: absolute; left: 0; top: 150px;
    width: 10px; height: 34px;
    background: var(--brand-blue);
    border-radius: 0 3px 3px 0;
  }
  .identity { position: absolute; left: 46px; top: 130px; }
  .identity__name {
    font-weight: 800; font-size: 26px; letter-spacing: 0.5px;
    color: var(--brand-blue); line-height: 1;
  }
  .identity__title {
    font-weight: 400; font-size: 14px; color: var(--text-grey);
    margin-top: 6px; letter-spacing: 0.4px;
  }
  .contacts { position: absolute; left: 46px; top: 196px; list-style: none; }
  .contacts__item {
    display: flex; align-items: center; gap: 8px;
    font-size: 14px; color: var(--text-dark); line-height: 22px;
  }
  .contacts__icon { width: 14px; height: 14px; flex: none; }
  .brand {
    display: flex; align-items: center; gap: 12px;
    font-weight: 500; font-size: 30px; letter-spacing: 4px;
  }
  .brand__square { width: 16px; height: 16px; background: var(--brand-blue); }
  .card--front .brand { position: absolute; right: 44px; top: 70px; color: var(--text-dark); }
  /* Back */
  .card--back {
    background: radial-gradient(circle at 40% 30%, #2a2a2a 0%, var(--card-black) 70%);
  }
  .card--back .brand { position: absolute; left: 56px; top: 118px; color: var(--text-light); }
  .card--back .brand__square { background: var(--accent-cyan); }
  .tagline {
    position: absolute; right: 64px; top: 0; bottom: 0;
    writing-mode: vertical-rl; transform: rotate(180deg);
    white-space: nowrap; text-align: center;
    font-weight: 600; font-size: 16px; letter-spacing: 1px;
    color: var(--text-light);
  }
  .tagline__accent { color: var(--accent-cyan); }
</style>
</head>
<body>
  <section class="card card--front" aria-label="Card front">
    <span class="card__tab"></span>
    <div class="brand"><span class="brand__square"></span>VELTRIX</div>
    <div class="identity">
      <h1 class="identity__name">DANIEL HARPER</h1>
      <p class="identity__title">Managing Director</p>
    </div>
    <ul class="contacts">
      <li class="contacts__item">
        <svg class="contacts__icon" viewBox="0 0 16 16"><path fill="#1e7fd0" d="M3 1l3 3-2 2c1 2 3 4 5 5l2-2 3 3-2 3C6 15 1 10 1 3z"/></svg>
        044-555 010 234
      </li>
      <li class="contacts__item">
        <svg class="contacts__icon" viewBox="0 0 16 16"><rect x="1" y="3" width="14" height="10" rx="1" fill="#1e7fd0"/><path d="M1 4l7 5 7-5" stroke="#fff" stroke-width="1.4" fill="none"/></svg>
        info@veltrixmail.example
      </li>
      <li class="contacts__item">
        <svg class="contacts__icon" viewBox="0 0 16 16"><circle cx="8" cy="8" r="7" fill="#1e7fd0"/><path d="M1 8h14M8 1c-3 4-3 10 0 14M8 1c3 4 3 10 0 14" stroke="#fff" stroke-width="1.2" fill="none"/></svg>
        www.withveltrix.example
      </li>
    </ul>
  </section>

  <section class="card card--back" aria-label="Card back">
    <div class="brand"><span class="brand__square"></span>VELTRIX</div>
    <p class="tagline">CONFIDENCE IN <span class="tagline__accent">MOTION</span></p>
  </section>
</body>
</html>
```